New company looking for logo, for business cards and email signature.
we provide Safety, Training and Project Management Services to Mining and Transport sectors.

HALVORN CONSULTANCY, Tom Ashcrove, Principal Consultant, 0491362817, halvornconsultancy@postvale.example , Unit 412,KestwickRidge Business Hub,817 Tulloch Road, Carrowby, 4832.
Dependable Operations built on Care, Competence and Guidance.

```html
<!DOCTYPE html>
<html lang="en">
<head>
<meta charset="utf-8">
<title>Halvorn Consultancy – Business Cards</title>
<link rel="stylesheet" href="https://fonts.googleapis.com/css2?family=Archivo:wght@400;700;800&display=swap">
<style>
  :root {
    --backdrop: #e4e4e4;
    --card-light: #f7f7f5;
    --card-dark: #141414;
    --ink: #111111;
    --ink-soft: #2b2b2b;
    --paper-white: #f2f2f2;
    --rule: #1a1a1a;
  }
  * { box-sizing: border-box; margin: 0; padding: 0; }
  html, body {
    width: 1200px;
    height: 900px;
    overflow: hidden;
    background: var(--backdrop);
    font-family: "Archivo", "Helvetica Neue", Arial, sans-serif;
  }
  .stage {
    width: 1200px;
    height: 900px;
    display: flex;
    align-items: center;
    justify-content: center;
    gap: 60px;
  }
  .card {
    width: 500px;
    height: 300px;
    border-radius: 3px;
    box-shadow: 0 10px 24px rgba(0,0,0,0.14), 0 2px 4px rgba(0,0,0,0.08);
  }

  /* Contact side */
  .card--contact {
    background: var(--card-light);
    color: var(--ink);
    padding: 34px 40px 0 40px;
    position: relative;
  }
  .contact__name {
    font-weight: 800;
    font-size: 34px;
    letter-spacing: 0.5px;
    line-height: 1;
    text-transform: uppercase;
  }
  .contact__role {
    margin-top: 6px;
    font-weight: 400;
    font-size: 13px;
    letter-spacing: 1px;
    color: var(--ink-soft);
  }
  .contact__list {
    list-style: none;
    margin-top: 16px;
  }
  .contact__item {
    display: flex;
    align-items: flex-start;
    gap: 8px;
    font-size: 13.5px;
    line-height: 1.3;
    margin-bottom: 6px;
  }
  .contact__icon {
    flex: 0 0 14px;
    width: 14px;
    height: 14px;
    margin-top: 1px;
  }
  .contact__rule {
    position: absolute;
    left: 40px;
    right: 28px;
    height: 1.5px;
    background: var(--rule);
  }
  .contact__rule--top { top: 218px; }
  .contact__rule--bottom { top: 262px; }
  .contact__tagline {
    position: absolute;
    left: 40px;
    right: 28px;
    top: 232px;
    font-weight: 700;
    font-size: 11.5px;
    white-space: nowrap;
  }

  /* Brand side */
  .card--brand {
    background: var(--card-dark);
    display: flex;
    align-items: center;
    justify-content: center;
  }
  .brand {
    display: flex;
    align-items: center;
    gap: 16px;
    color: var(--paper-white);
  }
  .brand__square {
    width: 40px;
    height: 40px;
    background: var(--paper-white);
  }
  .brand__name {
    font-weight: 800;
    font-size: 30px;
    line-height: 1.05;
    letter-spacing: 1px;
  }
</style>
</head>
<body>
  <main class="stage">
    <section class="card card--contact" aria-label="Contact side">
      <h1 class="contact__name">Tom Ashcrove</h1>
      <p class="contact__role">PRINCIPAL CONSULTANT</p>
      <ul class="contact__list">
        <li class="contact__item">
          <svg class="contact__icon" viewBox="0 0 14 14" aria-hidden="true">
            <circle cx="7" cy="7" r="6.3" fill="none" stroke="#111" stroke-width="1.2"/>
            <path d="M4.6 3.8c.5-.4 1-.2 1.2.3l.4.9c.1.3 0 .6-.2.8l-.4.3c.4.9 1 1.5 1.9 1.9l.3-.4c.2-.2.5-.3.8-.2l.9.4c.5.2.7.7.3 1.2-.6.7-1.5.8-2.4.3-1.4-.7-2.5-1.8-3.2-3.2-.4-.9-.3-1.7.4-2.3z" fill="#111"/>
          </svg>
          <span>0491362817</span>
        </li>
        <li class="contact__item">
          <svg class="contact__icon" viewBox="0 0 14 14" aria-hidden="true">
            <rect x="0.5" y="2.5" width="13" height="9" fill="#111"/>
            <path d="M0.8 3l6.2 4.8L13.2 3" fill="none" stroke="#f7f7f5" stroke-width="1"/>
          </svg>
          <span>halvornconsultancy@postvale.example</span>
        </li>
        <li class="contact__item">
          <svg class="contact__icon" viewBox="0 0 14 14" aria-hidden="true">
            <path d="M7 0.5a4.5 4.5 0 0 0-4.5 4.5c0 3.3 4.5 8.5 4.5 8.5s4.5-5.2 4.5-8.5A4.5 4.5 0 0 0 7 0.5z" fill="#111"/>
            <circle cx="7" cy="5" r="1.6" fill="#f7f7f5"/>
          </svg>
          <span>Unit 412,KestwickRidge Business Hub,<br>817 Tulloch Road, Carrowby, 4832</span>
        </li>
      </ul>
      <div class="contact__rule contact__rule--top"></div>
      <p class="contact__tagline">Dependable Operations built on Care, Competence and Guidance.</p>
      <div class="contact__rule contact__rule--bottom"></div>
    </section>

    <section class="card card--brand" aria-label="Brand side">
      <div class="brand">
        <span class="brand__square" aria-hidden="true"></span>
        <p class="brand__name">HALVORN<br>CONSULTANCY</p>
      </div>
    </section>
  </main>
</body>
</html>
```